Business Stationery - Business Cards - Letterheads, Compliment Slips

We need a new set of artwork designed for our client, they are a Construction Company, that also sell Kitchens, bathrooms and appliances.
They are an up and comping company that focus on quality and bespoke build. For them it is all about the quality of what they install, build or design. They have recently been awarded sole distributorship of a German kitchen brand Hannelore Moebel.
We need to present a quick job to them and provide some proofs for their new Artwork which encompasses all the elements of the company
The company name is the Tassel Group and we need to design a logo also.
Any Questions please let me know asap

Target Market(s)
Upmarket clients, or small Development companies.
Industry/Entity Type
Business
Look and feel
Each slider illustrates characteristics of the customer's brand and the style your logo design should communicate.

```html
<!DOCTYPE html>
<html lang="en">
<head>
<meta charset="utf-8">
<title>Tassel Group – Compliment Slip</title>
<link href="https://fonts.googleapis.com/css2?family=Tinos&display=swap" rel="stylesheet">
<style>
  :root {
    --page: #ffffff;
    --panel: #39342f;
    --gold: #aba46b;
    --band-start: #96916a;
    --band-end: #bdb66a;
    --ink: #3a3632;
    --frame: #48443f;
  }
  * { margin: 0; padding: 0; box-sizing: border-box; }
  html, body {
    width: 1200px;
    height: 999px;
    overflow: hidden;
    background: var(--page);
    font-family: "Tinos", "Times New Roman", serif;
  }
  .slip {
    position: absolute;
    left: 75px;
    top: 251px;
    width: 1051px;
    height: 496px;
    border: 2px solid var(--frame);
    border-left-width: 1px;
    background: var(--page);
  }
  .brand-panel {
    position: absolute;
    left: 0;
    top: 0;
    width: 389px;
    height: 454px;
    background: var(--panel);
  }
  .brand-name {
    position: absolute;
    left: 0;
    width: 389px;
    top: 300px;
    display: flex;
    justify-content: center;
    align-items: center;
    gap: 12px;
    color: var(--gold);
    font-size: 36px;
    font-weight: 400;
    line-height: 1;
  }
  .brand-mark {
    width: 14px;
    height: 14px;
    background: var(--gold);
    flex: none;
  }
  .brand-band {
    position: absolute;
    left: 0;
    top: 454px;
    width: 389px;
    height: 40px;
    background: linear-gradient(90deg, var(--band-start), var(--band-end));
  }
  .panel-divider {
    position: absolute;
    left: 388px;
    top: 0;
    width: 1px;
    height: 494px;
    background: var(--frame);
  }
  .greeting {
    position: absolute;
    left: 389px;
    right: 0;
    top: 228px;
    text-align: center;
    color: var(--ink);
    font-size: 27px;
    letter-spacing: 0.3px;
  }
  .contact-row {
    position: absolute;
    left: 423px;
    top: 464px;
    display: flex;
    align-items: center;
    gap: 6px;
    color: var(--ink);
    font-size: 13.5px;
    white-space: nowrap;
  }
  .contact-item { display: flex; align-items: center; gap: 6px; margin-right: 2px; }
  .contact-item svg { width: 18px; height: 18px; flex: none; }
  .phone-number { letter-spacing: 1px; }
</style>
</head>
<body>
  <div class="slip">
    <div class="brand-panel">
      <div class="brand-name">
        <span class="brand-mark"></span>
        <span>Tassel Group</span>
      </div>
    </div>
    <div class="brand-band"></div>
    <div class="panel-divider"></div>

    <p class="greeting">With Best Compliments</p>

    <div class="contact-row">
      <span class="contact-item">
        <svg viewBox="0 0 18 18" aria-hidden="true"><circle cx="9" cy="9" r="9" fill="var(--gold)"/><path d="M5.6 4.6l1.8-.4 1 2.2-1 .9c.5 1.2 1.3 2 2.5 2.5l.9-1 2.2 1-.4 1.8c-3.8.2-7.2-3.2-7-7z" fill="#fff"/></svg>
        <span class="phone-number">321 555 01478</span>
      </span>
      <span class="contact-item">
        <svg viewBox="0 0 18 18" aria-hidden="true"><circle cx="9" cy="9" r="9" fill="var(--gold)"/><path d="M9 3.6a3.6 3.6 0 0 0-3.6 3.6c0 2.7 3.6 7 3.6 7s3.6-4.3 3.6-7A3.6 3.6 0 0 0 9 3.6z" fill="#fff"/><circle cx="9" cy="7.2" r="1.4" fill="var(--gold)"/></svg>
        <span>po box, city, state, zip</span>
      </span>
      <span class="contact-item">
        <svg viewBox="0 0 18 18" aria-hidden="true"><circle cx="9" cy="9" r="9" fill="var(--gold)"/><rect x="4.6" y="6" width="8.8" height="6" fill="#fff"/><path d="M4.6 6l4.4 3.3L13.4 6" fill="none" stroke="var(--gold)" stroke-width="1"/></svg>
        <span>reach@tasselgroup.com</span>
      </span>
      <span class="contact-item">
        <svg viewBox="0 0 18 18" aria-hidden="true"><circle cx="9" cy="9" r="9" fill="var(--gold)"/><rect x="0" y="6.6" width="18" height="4.8" fill="#fff"/><text x="9" y="10.6" text-anchor="middle" font-size="4.6" font-family="Tinos, serif" fill="var(--gold)">www</text></svg>
        <span>www.tasselgroup.com</span>
      </span>
    </div>
  </div>
</body>
</html>
```